Improve the UI for two Mobile Apps

Brevano licenses ERP software to mid-sized companies (50M plus). Brevano's product suite includes procurement, accounting and CRM applications.

We have two mobile Apps that integrate with our ERP applications - Tallyway Hub and Morrow Field Kit. The Tallyway Hub App allows a user to review and approve requisitions, purchase orders, supplier invoices and expense reports which are forwarded to the App from our ERP applications. The expense report App allows a user to enter travel expenses and attach photos of receipts.

We are satisfied with the functionality of both mobile Apps. Our goal is to improve the aesthetics (fonts, colors, graphics). We are looking for a clean, light weight, modern design. The design should also be consistent with our current Brevano colors (blue and green) and branding (see www.brevanosystems.com).

Documentation showing current screen shots for each App is attached (2 files).
Updates

Please focus on the 14 major forms in the attachment. The larger document includes about 40 forms. It is intended to illustrate the use of the Apps which hopefully is useful when considering design alternatives. We realize the budget may be insufficient for the complete redesign of both Apps. When accepting the final design we will negotiate a price for revising / completing all forms. At this point we will increase the project's budget or complete the remaining work in-house. Thanks, Derek...

Target Market(s)

We sell to mid-large sized corporations. Are primary customer is the purchasing agent.

Industry/Entity Type

Accounting

Number of Pages Required

5+ page

Requirements
Must have
• Clean, modern design of the major entry forms shown in the attached documents. I need graphics and colors only. Our developers will adjust the Apps. I have attached 2 sets of documents. The first 2 files illustrate the use of all forms in both apps. Several forms appear multiple times. The second set of 3 files include the unique forms in both apps (14 in total). These files are labeled "(major forms)".

```html
<!DOCTYPE html>
<html lang="en">
<head>
<meta charset="utf-8">
<title>Edit Trip Info</title>
<link rel="stylesheet" href="https://fonts.googleapis.com/css2?family=Arimo:wght@400&family=Roboto:wght@300;400&display=swap">
<style>
  :root {
    --status-black: #000000;
    --status-blue: #33b5e5;
    --brand-blue: #0158a9;
    --accent-green: #8cc152;
    --white: #ffffff;
    --tab-inactive: #f0f0f1;
    --line-grey: #c9cacc;
    --field-bg: #eff0f2;
    --text-dark: #1d1d1d;
    --nav-icon: #9a9a9a;
  }
  * { box-sizing: border-box; margin: 0; padding: 0; }
  html, body {
    width: 720px;
    height: 1200px;
    overflow: hidden;
    background: var(--white);
  }
  .screen {
    position: relative;
    width: 720px;
    height: 1200px;
    background: var(--white);
    font-family: "Arimo", Arial, sans-serif;
    color: var(--text-dark);
  }
  .status-bar {
    position: absolute;
    top: 0; left: 0;
    width: 720px; height: 46px;
    background: var(--status-black);
  }
  .status-bar svg { position: absolute; top: 0; left: 0; }
  .status-time {
    position: absolute;
    right: 12px; top: 6px;
    font-family: "Roboto", Arial, sans-serif;
    font-size: 28px;
    line-height: 34px;
    color: var(--status-blue);
  }
  .app-header {
    position: absolute;
    top: 46px; left: 0;
    width: 720px; height: 113px;
    background: var(--brand-blue);
  }
  .app-title {
    position: absolute;
    left: 0; right: 0; top: 0;
    line-height: 113px;
    text-align: center;
    font-family: "Roboto", Arial, sans-serif;
    font-weight: 300;
    font-size: 45px;
    color: var(--white);
  }
  .confirm-button {
    position: absolute;
    left: 624px; top: 23px;
  }
  .tabs {
    position: absolute;
    top: 159px; left: 0;
    width: 720px; height: 125px;
    display: flex;
  }
  .tab {
    height: 125px;
    display: flex;
    align-items: center;
    justify-content: center;
    font-family: "Roboto", Arial, sans-serif;
    font-size: 36px;
    color: var(--text-dark);
  }
  .tab--active {
    width: 362px;
    background: var(--white);
  }
  .tab--inactive {
    width: 358px;
    background: var(--tab-inactive);
    border-left: 2px solid var(--line-grey);
    border-bottom: 2px solid var(--line-grey);
  }
  .description-field {
    position: absolute;
    left: 42px; top: 344px;
    width: 635px; height: 615px;
    background: var(--field-bg);
    border: 2px solid var(--line-grey);
    border-radius: 9px;
    padding: 34px 30px 0 38px;
    font-size: 25.5px;
    line-height: 37.5px;
    color: var(--text-dark);
  }
  .nav-bar {
    position: absolute;
    left: 0; bottom: 0;
    width: 720px; height: 90px;
    background: var(--status-black);
  }
  .nav-bar svg { position: absolute; top: 0; left: 0; }
</style>
</head>
<body>
<main class="screen">
  <div class="status-bar">
    <svg width="720" height="46" viewBox="0 0 720 46" aria-hidden="true">
      <g class="wifi-icon" fill="var(--status-blue)">
        <path d="M562 38 L544 16 A28 28 0 0 1 580 16 Z"/>
      </g>
      <g class="signal-icon">
        <path d="M584 38 L610 10 L610 38 Z" fill="#4d4d4d"/>
        <path d="M584 38 L600 21 L600 38 Z" fill="var(--status-blue)"/>
      </g>
      <g class="battery-icon">
        <rect x="623" y="8" width="8" height="4" fill="var(--status-blue)"/>
        <rect x="619" y="12" width="16" height="27" fill="var(--status-blue)"/>
      </g>
    </svg>
    <span class="status-time">7:07</span>
  </div>

  <header class="app-header">
    <h1 class="app-title">Edit Trip Info</h1>
    <svg class="confirm-button" width="66" height="66" viewBox="0 0 66 66" role="img" aria-label="Save">
      <circle cx="33" cy="33" r="31" fill="var(--accent-green)" stroke="var(--white)" stroke-width="3"/>
      <path d="M19 34 L29 44 L47 23" fill="none" stroke="var(--white)" stroke-width="7" stroke-linecap="round" stroke-linejoin="round"/>
    </svg>
  </header>

  <nav class="tabs">
    <div class="tab tab--active">Description</div>
    <div class="tab tab--inactive">Accounting</div>
  </nav>

  <div class="description-field">
    Lorem Ipsum is simply dummy text of the<br>
    printing and typesetting industry. Lorem Ipsum<br>
    has been the industry's standard dummy text<br>
    ever since the 1500s, when an unknown<br>
    printer took a galley of type and scrambled it<br>
    to make a type specimen book. It has<br>
    survived not only five centuries, but also the<br>
    leap into electronic typesetting, remaining<br>
    essentially unchanged. It was popularised in<br>
    the 1960s with the release of Typeline sheets<br>
    containing Lorem Ipsum passages, and more<br>
    recently with desktop publishing software like<br>
    Folio Layout including versions of Lorem<br>
    Ipsum.
  </div>

  <div class="nav-bar">
    <svg width="720" height="90" viewBox="0 0 720 90" aria-hidden="true">
      <g fill="none" stroke="var(--nav-icon)" stroke-width="4" stroke-linejoin="round">
        <path class="back-icon" d="M126 24 L120 31 L126 38 M120 31 L168 31 A9 9 0 0 1 168 49 L134 49"/>
        <path class="home-icon" d="M327 46 L327 30 L360 18 L394 30 L394 46 Z"/>
        <g class="recent-icon">
          <rect x="540" y="30" width="40" height="19"/>
          <path d="M548 24 L586 24 L586 44"/>
          <path d="M556 18 L602 18 L602 38"/>
        </g>
      </g>
    </svg>
  </div>
</main>
</body>
</html>
```